Brisvale services brochure

We need a new company brochure. The brochure will be formatted for PDF distribution but should be printable on "letter" size paper. 2 pages plus front and back cover. Color white and same blue as logo. Logo "O" should be used as design. Look at webpage for general info: www.brisvale.ca<br/><br/>Front cover: pic1, logo, design and "Your Cleaning is Our Business". <br/>Back cover" "O" design, logo and info from "contact" page<br/>Front cover inside: design and intro from web home page, also use stock pics of clean offices ect as placeholders for purchased pics.<br/>1st page: design and "Our Services", use info of "Cleanroom & GMP Services", "Janitorial Services" from services page.<br/>2nd page: design and "Special Services", info from "Carpet & Upholstery Services", "Window Cleaning Services", and list of "Other Services".<br/>Back cover inside : design and info from technology page, use stock pics for place holders.

Industry/Entity Type

Janitorial

Font styles to use
Sans Serif
Other font styles liked:
• Futura Book

Colors
0555a3

Requirements
Must have
• The logo "O" (target) should be part of the design. Design color same as logo.

```html
<!DOCTYPE html>
<html lang="en">
<head>
<meta charset="utf-8">
<title>Brisvale – Quality Control &amp; Time Keeping</title>
<link rel="stylesheet" href="https://fonts.googleapis.com/css2?family=Ubuntu:wght@300;400&display=swap">
<style>
  :root {
    --brand-blue: #1a82c5;
    --text-grey: #4f4f4f;
    --heading-grey: #4a4a4a;
    --page-bg: #ffffff;
  }
  * { margin: 0; padding: 0; box-sizing: border-box; }
  html, body { width: 927px; height: 1200px; overflow: hidden; background: var(--page-bg); }
  body { font-family: "Ubuntu", sans-serif; color: var(--text-grey); }
  .page { position: relative; width: 927px; height: 1200px; overflow: hidden; }

  .section-banner { position: absolute; height: 62px; }
  .section-banner svg { position: absolute; inset: 0; }
  .section-banner h2 {
    position: absolute; top: 13px;
    font-weight: 300; font-size: 31px; color: #fff; letter-spacing: 0.2px; white-space: nowrap;
  }
  .banner-quality { left: 189px; top: 54px; width: 658px; }
  .banner-quality h2 { left: 29px; }
  .banner-time { left: 179px; top: 595px; width: 657px; }
  .banner-time h2 { left: 28px; }

  .copy { position: absolute; left: 190px; width: 670px; font-weight: 300; font-size: 16.3px; line-height: 24.2px; }
  .intro-quality { top: 135px; }
  .feature { margin-top: 4px; }
  .feature h3 { font-weight: 400; font-size: 19.5px; line-height: 26px; color: var(--heading-grey); margin-top: 2px; }
  .intro-time { top: 685px; }

  .staff-photo {
    position: absolute; left: 369px; top: 810px; width: 558px; height: 390px; z-index: 1;
    background: linear-gradient(180deg, #ffffff 0%, #eef1f5 45%, #c9d3e2 100%);
  }

  .realtime-list {
    position: absolute; left: 190px; top: 770px; width: 540px; z-index: 2;
    list-style: none; font-weight: 300; font-size: 16.3px; line-height: 24.2px;
  }
  .realtime-list li { padding-left: 13px; position: relative; margin-bottom: 6px; }
  .realtime-list li::before { content: "•"; position: absolute; left: 0; }
</style>
</head>
<body>
<main class="page">

  <div class="section-banner banner-quality">
    <svg width="658" height="62" viewBox="0 0 658 62" aria-hidden="true">
      <path d="M18 0 H337 C350 0 354 6 362 14 C372 24 374 26 388 26 H640 A18 18 0 0 1 640 62 H18 A18 18 0 0 1 0 44 V18 A18 18 0 0 1 18 0 Z" fill="var(--brand-blue)"/>
    </svg>
    <h2>Quality Control System</h2>
  </div>

  <section class="copy intro-quality">
    <p>Brisvale supports a real time interactive system that monitors and manages customer satisfaction, providing its customers with the tools to control their customised services. Through the Brisvale online web based system, our customers have access and control of the following:</p>
    <div class="feature">
      <h3>Inspections</h3>
      <p>Track trends to improve service, Perform detailed inspections, Track job performance, Correct deficiencies.</p>
    </div>
    <div class="feature">
      <h3>Work order management</h3>
      <p>Instantly distribute work orders to those responsible, Automatically escalate work orders to management, Single point communications, Change/Cancel work orders.</p>
    </div>
    <div class="feature">
      <h3>Job Scheduling</h3>
      <p>Track complience to contract specifications, Customize schedules to customer needs, Record daily and periodic services, Set automatic reminders.</p>
    </div>
    <div class="feature">
      <h3>Reports</h3>
      <p>Identify which areas of a building require more attention, Address employee issues found during an inspection Outline services that need specific treatment, Productivity tracking and control, Quality tracking and statistics, Communications statistics.</p>
    </div>
  </section>

  <div class="section-banner banner-time">
    <svg width="657" height="62" viewBox="0 0 657 62" aria-hidden="true">
      <path d="M18 0 H343 C356 0 360 6 368 14 C378 24 380 26 394 26 H639 A18 18 0 0 1 639 62 H18 A18 18 0 0 1 0 44 V18 A18 18 0 0 1 18 0 Z" fill="var(--brand-blue)"/>
    </svg>
    <h2>Automated Time Keeping</h2>
  </div>

  <p class="copy intro-time">Brisvale meets the increasing need for information accuracy and reliability with a computerised timekeeping system. Brisvale has realtime control of employees:</p>

  <div class="staff-photo" role="img" aria-label="Photo of a team of smiling cleaning staff in uniforms with a vacuum cleaner and buckets of cleaning supplies"></div>

  <ul class="realtime-list">
    <li>Realtime employee communications to improve morale and engagement to better service our customers</li>
    <li>Realtime management reporting</li>
    <li>Realtime no show alerts</li>
    <li>Realtime on site attendance</li>
  </ul>

</main>
</body>
</html>
```